【依頼の目的/概要】
電子書籍(lumora)の表紙デザインをお願いします。

【画像サイズ】 ※RZBより抜粋
表紙ファイルの理想的な寸法 2,560×1,600ピクセルです。
注:画像の寸法は 1,000×625ピクセル以上であることが必要です。
画像の最大の寸法は 10,000×10,000ピクセルです。

【タイトル】

5つの航路・ヴォルテノ大年譜など
人類普遍の必読真理書をギュっと1冊にまとめました

【著者】

RUNO

【本の内容】

5つの航路・ヴォルテノ大年譜などの人間心理・成功本を
まとめて解説した本です。

※本文を参考資料として添付します。

【デザイン要望】

特にイメージにこだわりはありませんので、
自由な発送でのデザインご応募を楽しみにしています。

※次点の方への参加報酬を設定致しました。

※その他 必要な情報がありましたら、お問い合わせください。

```html
<!DOCTYPE html>
<html lang="ja">
<head>
<meta charset="utf-8">
<title>人類普遍の真理 — RUNO</title>
<link rel="stylesheet" href="https://fonts.googleapis.com/css2?family=Noto+Sans+JP:wght@700;900&family=Noto+Serif+JP:wght@500;600&display=swap">
<style>
  :root {
    --sky-light: #4fb6e6;
    --sky-mid: #2a93cf;
    --sky-deep: #1877b8;
    --stone-light: #f6f6f6;
    --stone-mid: #e2e3e4;
    --stone-dark: #c9cbcd;
    --label-blue: #1b8fd6;
    --ink: #222222;
    --white: #ffffff;
  }
  * { margin: 0; padding: 0; box-sizing: border-box; }
  html, body { width: 750px; height: 1200px; overflow: hidden; background: var(--white); }
  .cover {
    position: relative;
    width: 750px;
    height: 1200px;
    overflow: hidden;
    background: linear-gradient(180deg, var(--stone-light) 50%, var(--stone-mid) 80%, var(--stone-dark) 100%);
  }
  .cover-texture {
    position: absolute;
    left: 0; top: 0;
    width: 750px; height: 600px;
    background:
      radial-gradient(ellipse at 25% 30%, rgba(255,255,255,0.22), transparent 55%),
      radial-gradient(ellipse at 80% 70%, rgba(10,80,150,0.35), transparent 60%),
      linear-gradient(160deg, var(--sky-light) 0%, var(--sky-mid) 50%, var(--sky-deep) 100%);
  }
  .title {
    position: absolute;
    left: 0; top: 0;
    width: 750px;
    text-align: center;
    font-family: "Noto Serif JP", serif;
    color: var(--white);
  }
  .title-lead {
    position: absolute;
    left: 0; right: 0; top: 55px;
    font-size: 92px;
    font-weight: 500;
    letter-spacing: 4px;
    line-height: 1;
  }
  .title-main {
    position: absolute;
    left: 0; right: 0; top: 175px;
    font-size: 262px;
    font-weight: 600;
    letter-spacing: 6px;
    line-height: 1;
  }
  .title-question {
    position: absolute;
    left: 0; right: 0; top: 500px;
    font-size: 48px;
    font-weight: 500;
    line-height: 1;
    padding-left: 110px;
  }
  .featured {
    position: absolute;
    left: 82px; top: 628px;
    font-family: "Noto Sans JP", sans-serif;
  }
  .featured-row {
    display: flex;
    align-items: center;
    margin-bottom: 38px;
  }
  .featured-label {
    display: inline-block;
    background: var(--label-blue);
    color: var(--white);
    font-size: 55px;
    font-weight: 900;
    line-height: 1;
    padding: 16px 22px 18px;
    border-radius: 6px;
    letter-spacing: 1px;
  }
  .featured-etc {
    font-size: 40px;
    font-weight: 700;
    color: var(--ink);
    margin-left: 18px;
    align-self: flex-end;
  }
  .summary {
    position: absolute;
    left: 82px; top: 870px;
    font-family: "Noto Sans JP", sans-serif;
    font-weight: 900;
    font-size: 46px;
    line-height: 72px;
    color: var(--ink);
    letter-spacing: 1px;
  }
  .author {
    position: absolute;
    left: 0; right: 0; top: 1105px;
    text-align: center;
    font-family: "Noto Sans JP", sans-serif;
    font-weight: 900;
    color: var(--ink);
  }
  .author-label { font-size: 22px; margin-right: 14px; vertical-align: middle; }
  .author-name { font-size: 44px; letter-spacing: 2px; vertical-align: middle; }
</style>
</head>
<body>
  <main class="cover">
    <div class="cover-texture" role="img" aria-label="青い水彩風のテクスチャ背景"></div>
    <h1 class="title">
      <span class="title-lead">人類普遍の</span>
      <span class="title-main">真理</span>
      <span class="title-question">あなたは知っていますか?</span>
    </h1>
    <section class="featured">
      <div class="featured-row"><span class="featured-label">5つの航路</span></div>
      <div class="featured-row"><span class="featured-label">ヴォルテノ大年譜</span><span class="featured-etc">など</span></div>
    </section>
    <p class="summary">人類普遍の必読真理書を<br>ギュっと1冊にまとめました。</p>
    <p class="author"><span class="author-label">著者</span><span class="author-name">RUNO</span></p>
  </main>
</body>
</html>
```